Paper Towel Design - comparable to Plumrix, Toldex, Wendrove, Quor

1.I needed a design for a new product, PAPER TOWEL
2. Name: MARVOLIN (Trademark)
3. One word with letters TM for a trademark at the end of the name
4. Include: SNIP-N-FOLD this pertains to sheet size of 11 inches x 6 inches
5. Include: 100 percent biodegradable
6. Include: STRONG & ABSORBENT
7. Include the words Paper Towel

Hoxley Market(s)

Household, store, businesses (Online, Fennick, Brulio, Hoxley)

Industry/Entity Type

Paper Product

Font styles to use
Script

Colors
6b449b
33a6d7
fbee3e

Requirements
Must have
• vibrant color - striking design
Nice to have
• Excellent color combination of cyan, yellow, and purple
Should not have
• Should not be suggestive of any similar product, it should be unique and has its own identity

```html
<!DOCTYPE html>
<html lang="en">
<head>
<meta charset="utf-8">
<title>Marvolin Paper Towels – Package Label</title>
<link rel="stylesheet" href="https://fonts.googleapis.com/css2?family=Pacifico&family=Roboto:wght@300;400;900&display=swap">
<style>
  :root {
    --lime-light: #f2ec3c;
    --lime: #dbe22a;
    --lime-deep: #c9d81e;
    --white: #ffffff;
    --blue-deep: #1c7cc3;
    --blue-mid: #33a6d7;
    --blue-light: #8fd0ec;
    --purple: #6b449b;
    --yellow: #fbee3e;
    --leaf-green: #7c8f12;
  }
  html, body {
    margin: 0;
    padding: 0;
    overflow: hidden;
    background: var(--white);
  }
  .label {
    width: 1200px;
    height: 600px;
    display: block;
  }
  .script { font-family: "Pacifico", cursive; }
  .sans { font-family: "Roboto", Arial, sans-serif; }
  .brand-name { font-size: 118px; fill: var(--white); }
  .trademark { font-size: 40px; font-weight: 900; fill: var(--white); }
  .tagline-strong { font-size: 80px; fill: url(#taglineBlue); }
  .tagline-amp { font-size: 112px; fill: var(--yellow); }
  .tagline-absorbent { font-size: 70px; fill: url(#taglineBlueLight); }
  .product-type { font-size: 24px; font-weight: 300; letter-spacing: 1px; fill: var(--blue-mid); }
  .sheet-size { font-size: 46px; font-weight: 900; fill: var(--white); }
  .sheet-format { font-size: 34px; font-weight: 300; letter-spacing: 1px; fill: var(--white); }
  .eco-ring { fill: none; stroke: var(--white); stroke-width: 5; }
  .eco-ribbon-text { font-size: 20px; font-weight: 900; fill: var(--leaf-green); }
</style>
</head>
<body>
<svg class="label" viewBox="0 0 1200 600" xmlns="http://www.w3.org/2000/svg">
  <defs>
    <linearGradient id="limeField" x1="0" y1="0" x2="1" y2="0">
      <stop offset="0" stop-color="var(--lime-light)"/>
      <stop offset="1" stop-color="var(--lime-deep)"/>
    </linearGradient>
    <linearGradient id="bannerBlue" x1="0" y1="0" x2="1" y2="0">
      <stop offset="0" stop-color="var(--blue-deep)"/>
      <stop offset="1" stop-color="var(--blue-light)"/>
    </linearGradient>
    <linearGradient id="sizeBlue" x1="0" y1="0" x2="1" y2="0">
      <stop offset="0" stop-color="var(--blue-deep)"/>
      <stop offset="1" stop-color="var(--blue-light)"/>
    </linearGradient>
    <linearGradient id="taglineBlue" x1="0" y1="0" x2="1" y2="0">
      <stop offset="0" stop-color="var(--blue-deep)"/>
      <stop offset="1" stop-color="var(--blue-mid)"/>
    </linearGradient>
    <linearGradient id="taglineBlueLight" x1="0" y1="0" x2="1" y2="0">
      <stop offset="0" stop-color="var(--blue-mid)"/>
      <stop offset="1" stop-color="var(--blue-deep)"/>
    </linearGradient>
  </defs>

  <!-- background field -->
  <rect class="field" width="1200" height="600" fill="url(#limeField)"/>

  <!-- white sweep -->
  <path class="white-sweep" fill="var(--white)"
        d="M650 0 L1200 0 L1200 170 C980 260 780 420 640 600 L0 600 L0 400 C160 330 300 280 420 170 C500 95 570 40 650 0 Z"/>

  <!-- brand banner -->
  <g class="brand-banner">
    <path class="banner-fold" fill="var(--purple)"
          d="M382 112 L352 205 C362 240 382 258 402 262 Z"/>
    <path class="banner-wave" fill="url(#bannerBlue)"
          d="M380 110 C560 40 700 170 900 110 C1000 80 1100 60 1170 55 C1160 150 1140 250 1110 330 C960 300 800 330 650 290 C560 265 470 250 400 262 Z"/>
    <text class="script brand-name" x="760" y="235" text-anchor="middle">Marvolin</text>
    <text class="sans trademark" x="1118" y="185">™</text>
  </g>

  <!-- tagline -->
  <g class="tagline">
    <text class="script tagline-strong" x="262" y="340">Strong</text>
    <text class="script tagline-amp" x="270" y="455">&amp;</text>
    <text class="script tagline-absorbent" x="372" y="438">Absorbent</text>
    <text class="sans product-type" x="604" y="474">PAPER TOWELS</text>
  </g>

  <!-- sheet size panel -->
  <g class="sheet-size-panel">
    <path fill="url(#sizeBlue)" d="M0 485 C200 465 560 465 650 600 L0 600 Z"/>
    <text class="sans sheet-size" x="300" y="542" text-anchor="middle">11” x 6”</text>
    <text class="sans sheet-format" x="300" y="588" text-anchor="middle">SNIP-N-FOLD</text>
  </g>

  <!-- eco badge -->
  <g class="eco-badge">
    <circle class="eco-ring" cx="1090" cy="490" r="76"/>
    <circle cx="1090" cy="482" r="40" fill="var(--white)" opacity="0.85"
            role="img" aria-label="Leaf icon for biodegradable claim"/>
    <g transform="rotate(-12 1092 560)">
      <rect x="985" y="540" width="214" height="40" rx="4" fill="var(--white)"/>
      <text class="sans eco-ribbon-text" x="1092" y="567" text-anchor="middle">100% Biodegradable</text>
    </g>
  </g>
</svg>
</body>
</html>
```